Postcard Design

We need a double sided oversized postcard for a new Chiropractic office that focuses on wellness care.
My website is HollerbackChiroSC.com and possibly follow some of the colors and style of the website.
Updates

This is the link to the requirements to sending the mail. "Each Porch Prompt Post". See the top of the page looking at the requirements of the postage and address label. I would like to use more of the postage side of the flyer. https://www.parcelvane.example/business/pdf/quick-reference-guide.pdf I would also like to add the face picture of me from my brochure or I can upload an image if needed.

Project Deadline Extended
Reason: I will be unexpectedly out of town for remainder of week and wont have time to respond to designers.

The Massage is no longer coming soon. Please change the post card to show: Massage Thank you

Target Market(s)

General people who dont know about chiropractic. Help people to understand chiropractic is safe, natural and cost effective.

Chiropractic should be your first choice for health care to avoid unnecessary drugs or surgery.

Industry/Entity Type

Wellness

Requirements
Must have
• Add in "Call for a Complimentary Consultation"

```html
<!DOCTYPE html>
<html lang="en">
<head>
<meta charset="utf-8">
<title>Hollerback Family Chiropractic – Wellness Postcard</title>
<link href="https://fonts.googleapis.com/css2?family=Crimson+Pro:wght@400;600&family=Lato:ital,wght@0,400;0,700;0,900;1,700;1,900&family=Roboto:ital,wght@1,900&display=swap" rel="stylesheet">
<style>
  :root {
    --sky: #7fcdf2;
    --sky-deep: #3fa9e6;
    --navy: #0f3a78;
    --royal: #1565b0;
    --ink: #222a33;
    --white: #ffffff;
    --orange-a: #f0a01e;
    --orange-b: #e3531c;
    --grey: #7d7d7d;
    --page: #ffffff;
  }
  * { box-sizing: border-box; margin: 0; padding: 0; }
  html, body { width: 890px; height: 1200px; overflow: hidden; background: var(--page); }
  body { position: relative; font-family: "Lato", sans-serif; }

  .card { position: absolute; left: 24px; width: 836px; box-shadow: 0 3px 9px rgba(0,0,0,.35); overflow: hidden; }

  /* Front */
  .front { top: 24px; height: 549px; background: var(--sky); }
  .front__headline {
    position: absolute; top: 26px; left: 0; width: 100%; text-align: center;
    font-family: "Roboto", sans-serif; font-style: italic; font-weight: 900;
    font-size: 37px; color: var(--navy); letter-spacing: .3px;
    text-shadow: 0 0 4px #fff, 0 0 8px #fff;
  }
  .photo { position: absolute; width: 128px; height: 128px; border-radius: 8px; border: 1px solid rgba(15,58,120,.55); }
  .photo--hands   { left: 20px;  top: 89px;  background: linear-gradient(135deg, #e9b58e, #b56f4a); }
  .photo--back    { left: 154px; top: 131px; background: linear-gradient(160deg, #f3f1ee 20%, #8a5534 60%, #4a2a18); }
  .photo--massage { left: 288px; top: 101px; background: linear-gradient(150deg, #f0d7b3, #e8c39a 50%, #c49368); }
  .photo--produce { left: 421px; top: 164px; background: linear-gradient(135deg, #d2321e, #e8a21c 45%, #5f8a2a); }
  .photo--yoga    { left: 555px; top: 101px; background: linear-gradient(180deg, #b9d7f0 0%, #d6e7f3 45%, #67a333 55%, #3f7a1d 100%); }
  .photo--weights { left: 690px; top: 180px; background: linear-gradient(135deg, #f2f2f0, #d9c3ad 55%, #3a3a3a); }

  .front__mark { position: absolute; left: 22px; top: 250px; width: 120px; height: 240px; border-radius: 50%; background: var(--sky-deep); }
  .front__name {
    position: absolute; right: 26px; top: 278px; text-align: right;
    font-family: "Crimson Pro", serif; font-weight: 400; color: var(--white);
  }
  .front__name-main { display: block; font-size: 128px; line-height: .95; }
  .front__name-sub { display: block; font-family: "Lato", sans-serif; font-weight: 400; color: var(--white); font-size: 33px; letter-spacing: 3.4px; margin-top: 26px; }

  /* Back */
  .back { top: 612px; height: 542px; background: var(--white); }
  .services { position: absolute; left: 0; top: 0; width: 358px; height: 100%; background: var(--royal); color: var(--white); padding: 22px 20px 0 22px; }
  .services__brand { display: flex; align-items: center; gap: 12px; margin-bottom: 24px; }
  .services__dot { width: 58px; height: 58px; border-radius: 50%; background: var(--sky); flex: none; }
  .services__name { font-family: "Crimson Pro", serif; font-weight: 400; color: var(--white); line-height: 1; }
  .services__name b { display: block; font-weight: 400; font-size: 46px; }
  .services__name span { display: block; font-size: 15px; letter-spacing: 1.2px; text-transform: uppercase; margin-top: 2px; }
  .services__intro { font-weight: 900; font-style: italic; font-size: 12.4px; line-height: 1.3; margin-bottom: 12px; }
  .services__list { list-style: none; }
  .services__item { font-size: 10.6px; line-height: 1.36; margin-bottom: 9px; }
  .services__item strong { font-weight: 700; font-size: 12px; }
  .services__web { position: absolute; bottom: 12px; left: 0; width: 100%; text-align: center; font-weight: 900; font-size: 13px; letter-spacing: .6px; }

  .mailer { position: absolute; left: 358px; top: 0; right: 0; height: 100%; }
  .mailer__headline {
    position: absolute; left: 30px; top: 26px;
    font-family: "Crimson Pro", serif; font-weight: 600; font-size: 47px; line-height: .93;
    background: linear-gradient(180deg, var(--orange-a), var(--orange-b));
    -webkit-background-clip: text; background-clip: text; color: transparent;
  }
  .mailer__headline span { display: block; padding-left: 8px; }
  .indicia { position: absolute; right: 36px; top: 30px; width: 100px; text-align: center; font-family: "Crimson Pro", serif; font-size: 13.5px; line-height: 1.22; color: var(--grey); }
  .cta { position: absolute; left: 0; right: 0; top: 135px; height: 101px; background: var(--royal); color: var(--white); text-align: center; padding-top: 14px; }
  .cta__lead { font-weight: 700; font-size: 19px; }
  .cta__phone { display: inline-flex; align-items: center; gap: 10px; font-weight: 900; font-size: 35px; margin-top: 6px; }
  .cta__phone svg { width: 36px; height: 28px; }
  .recipient { position: absolute; right: 40px; top: 246px; width: 120px; text-align: center; font-family: "Crimson Pro", serif; font-size: 14px; line-height: 1.25; color: var(--grey); }
</style>
</head>
<body>

<section class="card front">
  <h1 class="front__headline">YOUR JOURNEY TO WELLNESS BEGINS HERE</h1>
  <div class="photo photo--hands" role="img" aria-label="Photo of hands massaging a shoulder"></div>
  <div class="photo photo--back" role="img" aria-label="Photo of a man's muscular back"></div>
  <div class="photo photo--massage" role="img" aria-label="Photo of a woman relaxing during a massage"></div>
  <div class="photo photo--produce" role="img" aria-label="Photo of fresh tomatoes, peppers and vegetables"></div>
  <div class="photo photo--yoga" role="img" aria-label="Photo of a woman in a yoga pose on a grassy field"></div>
  <div class="photo photo--weights" role="img" aria-label="Photo of a woman lifting a dumbbell"></div>
  <div class="front__mark"></div>
  <div class="front__name">
    <span class="front__name-main">Hollerback</span>
    <span class="front__name-sub">FAMILY CHIROPRACTIC</span>
  </div>
</section>

<section class="card back">
  <div class="services">
    <div class="services__brand">
      <div class="services__dot"></div>
      <div class="services__name"><b>Hollerback</b><span>Family Chiropractic</span></div>
    </div>
    <p class="services__intro">At Hollerback Family Chiropractic, we take great pride in providing the finest chiropractic care to each and every patient. We offer:</p>
    <ul class="services__list">
      <li class="services__item"><strong>Chiropractic Care:</strong> Advanced spinal correction and chiropractic adjustments utilizing "state of the art" chiropractic techniques.</li>
      <li class="services__item"><strong>Corrective Exercises:</strong> Special "blueprint" exercises to help strengthen and correct the irregularities in the body which may be causing pain.</li>
      <li class="services__item"><strong>Lifestyle Advice:</strong> Helpful "coaching" towards achieving a healthier lifestyle.</li>
      <li class="services__item"><strong>Nutritional Counseling:</strong> Specific recommendations on nutritional supplements and healthy food choices.</li>
      <li class="services__item"><strong>Massage Therapy:</strong> Our chiropractic office provides specific massage and muscular therapy that is complimentary to their chiropractic care.</li>
      <li class="services__item"><strong>Spinal &amp; Postural Screenings:</strong> Posture and spinal screenings by a trained and experienced chiropractor such as Dr. Dale Hollerback can help reveal important health information, unlocking the door to improved health and well-being. In order to help the Brookhaven community.</li>
    </ul>
    <p class="services__web">WWW.HOLLERBACKCHIROSC.COM</p>
  </div>

  <div class="mailer">
    <h2 class="mailer__headline">WELLNESS<span>AWAITS YOU</span></h2>
    <p class="indicia">PRSRT STD<br>EC RWSS<br>Local Postage<br>PAID<br>EPPP Retail.</p>
    <div class="cta">
      <p class="cta__lead">Call for a Complimentary Consultation</p>
      <p class="cta__phone">
        <svg viewBox="0 0 36 28" aria-hidden="true"><path d="M3 9c0-4 6-7 15-7s15 3 15 7v3h-8V8c-2-1-4-1-7-1s-5 0-7 1v4H3z" fill="currentColor"/><path d="M9 13h18l5 13H4z" fill="currentColor"/><circle cx="18" cy="19" r="3.2" fill="#1565b0"/></svg>
        843.555.0186
      </p>
    </div>
    <p class="recipient">Local<br>Postal Customer</p>
  </div>
</section>

</body>
</html>
```